New Template design for Website in Wordpress

We are interested in changing our website look at www.haulvantix.com -We also are very interested in Have it done in Wordpress in which we are understanding the search engines are liking a bit more. The website we would want to try working with on this is www.haulvantix.com. We look forward to seeing the different design ideas please just make sure they are in wordpress! Thanks, Merrick

Reason: need more design idea..... We would still like to use our pictures off our site since we paid for them so keep that in mind as well as we would still want the rotating pictures in the head of the page but not in Flash.

```html
<!DOCTYPE html>
<html lang="en">
<head>
<meta charset="utf-8">
<title>Haulvantix – A Diversified Freight Company</title>
<link rel="stylesheet" href="https://fonts.googleapis.com/css2?family=Source+Sans+3:wght@400;600;700&display=swap">
<style>
:root{
  --red:#c0302c;
  --red-dark:#a3170f;
  --red-text:#d42a20;
  --ink:#1b1b1b;
  --band:#101010;
  --strip:#0d0f14;
  --white:#ffffff;
  --panel:#ececec;
  --pin:#777777;
}
*{box-sizing:border-box;margin:0;padding:0}
html,body{width:1093px;height:1200px;overflow:hidden}
body{position:relative;background:var(--ink);font-family:Arial,Helvetica,sans-serif;color:var(--white)}
.abs{position:absolute}
.top-strip{left:0;top:0;width:1093px;height:23px;background:var(--strip)}
.flags{left:654px;top:6px;display:flex;gap:4px}
.flags span{width:14px;height:10px;background:#8a8f9a;border-radius:1px}
.lang{left:895px;top:4px;width:107px;height:15px;background:#fff;color:#222;font-size:9px;line-height:15px;padding-left:3px;border:1px solid #999}
.lang i{position:absolute;right:1px;top:1px;width:12px;height:11px;background:#bbb}
.header{left:0;top:23px;width:1093px;height:67px;background:linear-gradient(#c9332e,#b52925)}
.brand{left:91px;top:0;width:224px;height:105px;background:#1f1f1f;padding:14px 0 0 11px}
.brand-name{font-family:"Source Sans 3",sans-serif;font-weight:700;font-size:39px;line-height:40px;color:var(--white)}
.brand-tag{font-family:"Source Sans 3",sans-serif;font-size:15px;margin-top:8px;color:var(--white)}
.nav{height:47px;display:flex;font-family:"Source Sans 3",sans-serif;font-weight:600;font-size:12.5px}
.nav a{color:var(--white);text-decoration:none;border-left:1px solid #e06a64;border-right:1px solid #8f1d19;display:flex;align-items:center;justify-content:center}
.body-bg{left:0;top:90px;width:1093px;height:630px;background:linear-gradient(180deg,#262626,#1a1a1a 60%,#222)}
.slider{left:91px;top:118px;width:912px;height:348px;background:#fff;padding:5px}
.slider-photo{width:100%;height:100%;background:linear-gradient(100deg,#8fb6d8 0%,#c7d9e8 35%,#b23a33 60%,#c22a22 75%,#8aa6bf 100%)}
.caption{left:165px;top:179px;width:282px;height:106px;background:linear-gradient(#2e2e2e,#474747);padding:14px 0 0 16px;font-family:"Source Sans 3",sans-serif}
.caption b{display:block;color:var(--red-text);font-size:34px;line-height:36px;letter-spacing:1px}
.caption span{display:block;font-size:33px;line-height:40px;color:var(--white)}
.intro{left:0;top:488px;width:1093px;text-align:center}
.intro h1{font-family:"Source Sans 3",sans-serif;font-weight:700;color:var(--red-text);font-size:24px;line-height:30px;letter-spacing:1px}
.intro h2{font-family:"Source Sans 3",sans-serif;font-weight:400;color:#ddd;font-size:16px;line-height:20px;margin-top:-3px}
.intro p{font-size:11.2px;line-height:16.4px;width:880px;margin:9px auto 0}
.btn{display:inline-block;margin-top:12px;background:var(--red-text);color:#fff;font-size:11.5px;line-height:14px;border-radius:3px;padding:7px 8px;white-space:nowrap}
.services{left:0;top:720px;width:1093px;height:231px;background:var(--band)}
.svc{top:17px;width:201px}
.svc h3{font-family:"Source Sans 3",sans-serif;font-weight:600;font-size:17.5px;line-height:18px;padding-left:4px;height:40px}
.svc .photo{height:83px;border-radius:3px}
.svc p{font-size:11.2px;line-height:16.5px;margin-top:10px;padding-left:4px}
.more{margin-top:6px;padding-left:4px;display:flex;align-items:center;gap:7px;color:var(--red-text);font-size:12px}
.footer{left:0;top:951px;width:1093px;height:215px;background:var(--red-dark);font-size:11.5px;line-height:20px}
.contact{top:33px}
.contact a{color:#fff;text-decoration:underline}
.footer-brand{left:115px;top:133px;font-family:"Source Sans 3",sans-serif}
.footer-brand b{display:block;font-size:27px;line-height:30px;color:#eee}
.footer-brand span{display:block;font-size:16.5px;color:#ddd;letter-spacing:.5px}
.map{left:437px;top:22px;width:281px;height:173px;background:linear-gradient(135deg,#d9d9d9,#c4c4c4)}
.find{left:718px;top:22px;width:283px;height:173px;background:var(--panel);color:#333;padding:0 0 0 10px}
.find h4{font-weight:400;font-size:23px;margin-top:40px;color:#444}
.find p{font-size:11px;line-height:13px;margin-top:12px;width:230px}
.pin{right:0;top:0;width:47px;height:57px;background:var(--pin);display:flex;align-items:center;justify-content:center}
.bottom{left:0;top:1166px;width:1093px;height:34px;background:#1a1a1a;text-align:center;color:#ddd;font-size:12.5px;line-height:34px}
</style>
</head>
<body>
<div class="abs top-strip"></div>
<div class="abs flags"><span></span><span></span><span></span><span></span><span></span><span></span><span></span><span></span><span></span><span></span><span></span><span></span></div>
<div class="abs lang">English / English<i></i></div>

<header class="abs header">
  <nav class="abs nav" style="top:20px;left:585px">
    <a style="width:81px">HOME</a>
    <a style="width:178px">INSURANCE &amp; LEGAL INFO</a>
    <a style="width:158px">FAST FREIGHT QUOTE</a>
  </nav>
</header>
<div class="abs brand">
  <div class="brand-name">Haulvantix</div>
  <div class="brand-tag">A Diversified Freight Company</div>
</div>

<div class="abs body-bg" role="img" aria-label="Dimmed harbour photograph behind the content"></div>

<div class="abs slider">
  <div class="slider-photo" role="img" aria-label="Rotating header photo: red cargo ship moored beside a marina"></div>
</div>
<div class="abs caption"><b>A DIVERSIFIED</b><span>Freight Company</span></div>

<section class="abs intro">
  <h1>WORLDWIDE SHIPPING- OCEAN AND TRUCKING WITH NO LIMITS</h1>
  <h2>Personal, Professional &amp; Experienced</h2>
  <p>Welcome to Haulvantix and Broadline Freight Inc. We are a one stop solution logistics company servicing Worldwide with our Trucking and Ocean shipping service. In using our freight services, we will negotiate a competitive freight quote using over 5000 different carriers who are certified and contracted by us. We have all equipment types available daily, service all freight types, and have no limits Worldwide.</p>
  <p style="margin-top:17px">Whether you need a freight quote for a full load, LTL/Partial load, or Oversized Machinery or Equipment, trucking and/or ocean shipment, we will take care of it. All your freight or equipment to be shipped will be covered in full by our insurance with no limitations to match its value. We manage the calls, the paperwork, and the headaches, and you get your freight moved with no hassles at a competitive shipping price!</p>
  <span class="btn">More Information</span>
</section>

<section class="abs services">
  <div class="abs svc" style="left:112px">
    <h3>Heavy haul<br>services</h3>
    <div class="photo" role="img" aria-label="Heavy haul truck carrying industrial machinery" style="background:linear-gradient(#cfe0ef,#b7a78a 60%,#7a6a55)"></div>
    <p>Welcome to Haulvantix and Broad-line Freight Inc.</p>
    <div class="more"><svg width="15" height="15"><circle cx="7.5" cy="7.5" r="7.5" fill="#555"/><path d="M6 4l4 3.5L6 11z" fill="#111"/></svg>More info</div>
  </div>
  <div class="abs svc" style="left:337px">
    <h3>Dry and refrigerated<br>services</h3>
    <div class="photo" role="img" aria-label="White box truck for dry and refrigerated freight" style="background:linear-gradient(#f4f4f4,#dcdcdc 70%,#888)"></div>
    <p>Welcome to Haulvantix and Broad-line Freight Inc.</p>
    <div class="more"><svg width="15" height="15"><circle cx="7.5" cy="7.5" r="7.5" fill="#555"/><path d="M6 4l4 3.5L6 11z" fill="#111"/></svg>More info</div>
  </div>
  <div class="abs svc" style="left:564px">
    <h3>Flatbed, stepdeck &amp;<br>piggy bank services</h3>
    <div class="photo" role="img" aria-label="Blue truck pulling a flatbed trailer on a highway" style="background:linear-gradient(#8fb07a,#7f8a8a 45%,#4a5a7a)"></div>
    <p>Welcome to Haulvantix and Broad-line Freight Inc.</p>
    <div class="more"><svg width="15" height="15"><circle cx="7.5" cy="7.5" r="7.5" fill="#555"/><path d="M6 4l4 3.5L6 11z" fill="#111"/></svg>More info</div>
  </div>
  <div class="abs svc" style="left:788px">
    <h3>Freight forwading<br>ocean services</h3>
    <div class="photo" role="img" aria-label="Container ship at sea seen from above" style="background:linear-gradient(120deg,#1e5a7a,#3f7f8f 50%,#1a4a66)"></div>
    <p>Welcome to Haulvantix and Broad-line Freight Inc.</p>
    <div class="more"><svg width="15" height="15"><circle cx="7.5" cy="7.5" r="7.5" fill="#555"/><path d="M6 4l4 3.5L6 11z" fill="#111"/></svg>More info</div>
  </div>
</section>

<footer class="abs footer">
  <div class="abs contact" style="left:115px">HAULVANTIX<br>48 Larkmoor Court<br>Fairhaven,<br>KY 42190</div>
  <div class="abs contact" style="left:263px">Fax: (000) 555-0143<br>Phone: (000) 555-0142<br><a>Email: dispatch@haulvantix.com</a></div>
  <div class="abs footer-brand"><b>HAULVANTIX</b><span>A DIVERSIFIED FREIGHT COMPANY</span></div>
  <div class="abs map" role="img" aria-label="Street map showing the office location"></div>
  <div class="abs find">
    <div class="abs pin"><svg width="20" height="30" viewBox="0 0 20 30"><path d="M10 1a9 9 0 0 0-9 9c0 7 9 19 9 19s9-12 9-19a9 9 0 0 0-9-9z" fill="none" stroke="#fff" stroke-width="2"/><circle cx="10" cy="10" r="3.5" fill="none" stroke="#fff" stroke-width="2"/></svg></div>
    <h4>HOW TO FIND US?</h4>
    <p>Lorem ipsum dolor sit amet, consectetur adipisc elit. Proin ultricies vestibulum velit, bibendum et condimentum metusip dolore ipsum.</p>
  </div>
</footer>
<div class="abs bottom">© 2014 Copyright - haulvantix . All rights reserved</div>
</body>
</html>
```